Healing Arts Brochure with Simple, Elegant, Zen Design ,

I need to create a brochure for an upcoming event and I have to complete this project in the next few days.
I would like a tri-fold or z fold type of brochure- standard size of 8.5 x 11- both sides with text

i would like the overall design to be simple, elegant and zen .... yet not too plain :-))
I would like the fonts used to be clean and clear and ... easy to read.
I would like the background color to be white/cream or light color
Please do not use too many colors when working with the descriptions of my services or break those sections up too much ... a little is ok.
I don't want the brochure to be busy

I've uploaded the text, my photo, a photo that I will be using on my website, my logo symbol without my name and several logo symbols with my name in different font styles. I am not wed to any of the various font styles of the logo just yet.
TEXT FILE IS UPLOADED

Dear Designers, The design submissions that I'm receiving so far have not been including all 3 pages of text in the brochure. I pulled my text file to update it with the instructions that there are 3 pages of text information that need to be on the brochure. Unfortunately, I'm not able to upload the text file - seems to be a glitch on the ArtMarkly website.. I called for support and they won't get back to me for a couple of hours. That will be around 11:00 am PST in the USA. PLEASE CHECK BACK if you haven't already downloaded the text file. Otherwise, please add the missing information and resubmit your ideas. Thank you!! MR

Target Market(s)

My services target clients in the healing arts.

Industry/Entity Type

Event

Requirements
Must have
• Please include the colors tones of my logo and the sunset photo -golds, oranges, blues
Brochure must include my photo and the sunset photo
Should not have
• Objects like teacups etc. that have nothing to do with my services - thank you kindly
I don't want any other photos or objects on the brochure other than my photo and the sun
Please don't put the tagline in quotes
Please do not make the brochure busy with too many colors in the text.

```html
<!DOCTYPE html>
<html lang="en">
<head>
<meta charset="utf-8">
<title>Maren Rowe – Healing Arts Brochure</title>
<link href="https://fonts.googleapis.com/css2?family=Source+Sans+3:wght@300;400;600;700&display=swap" rel="stylesheet">
<style>
  :root {
    --paper: #ffffff;
    --ink: #1c1c1c;
    --frame: #3a3a3a;
    --gold: #ffcc33;
    --orange: #f08a12;
    --deep-orange: #e0600a;
    --wash-gold: rgba(255, 196, 90, 0.16);
    --wash-blue: rgba(150, 170, 215, 0.18);
  }
  * { box-sizing: border-box; margin: 0; padding: 0; }
  html, body { width: 1200px; height: 1000px; overflow: hidden; background: var(--paper); }
  body { font-family: "Source Sans 3", Arial, sans-serif; color: var(--ink); }

  .brochure { position: relative; width: 1200px; height: 1000px; background: var(--paper); }
  .brochure__frame { position: absolute; left: 26px; top: 56px; width: 1150px; height: 888px; border: 1px solid var(--frame); }

  .backdrop-glow {
    position: absolute; left: 27px; top: 57px; width: 1148px; height: 886px;
    background:
      radial-gradient(ellipse 420px 380px at 250px 780px, var(--wash-blue), transparent 70%),
      radial-gradient(ellipse 700px 620px at 560px 620px, var(--wash-gold), transparent 72%);
  }

  .block { position: absolute; font-weight: 300; font-size: 16.5px; line-height: 19.2px; }
  .block p { text-align: justify; text-indent: 52px; hyphens: auto; -webkit-hyphens: auto; }
  .block p + p { margin-top: 19px; }

  .photo-strip { position: absolute; left: 60px; top: 90px; width: 338px; height: 135px; display: flex; }
  .photo-strip__portrait { width: 127px; height: 100%; background: linear-gradient(160deg, #3e4a2c, #8c7a5c 55%, #d9b08c); }
  .photo-strip__sunset { flex: 1; height: 100%; background: radial-gradient(ellipse 90px 60px at 50% 28%, #fff6c8, #ffb320 45%, #e86a0c 85%), linear-gradient(#f49a1a, #d85a08); }
  .pointer { position: absolute; width: 0; height: 0; border-left: 6px solid transparent; border-right: 6px solid transparent; border-top: 8px solid var(--deep-orange); }

  .credentials { left: 60px; top: 247px; width: 340px; font-size: 16.5px; line-height: 19.3px; }
  .credentials__name { font-weight: 400; font-size: 17px; }

  .intro { left: 60px; top: 420px; width: 305px; font-size: 15.5px; line-height: 17.8px; }
  .intro p { text-align: left; text-indent: 52px; }

  .services-title { position: absolute; left: 60px; top: 595px; font-weight: 700; font-size: 18.5px; line-height: 21.5px; }
  .services-list { position: absolute; left: 113px; top: 698px; list-style: none; font-weight: 700; font-size: 18.5px; line-height: 22.5px; }
  .services-list li { padding-left: 12px; text-indent: -12px; }

  .section-tab {
    position: absolute; height: 42px; display: flex; align-items: center; padding-left: 14px;
    font-weight: 700; font-size: 17.5px; white-space: nowrap;
    background: linear-gradient(180deg, var(--gold) 0%, var(--orange) 60%, rgba(240,138,18,0.25) 100%);
  }
  .section-tab--somatic { left: 459px; top: 91px; width: 225px; }
  .section-tab--rest { left: 843px; top: 416px; width: 292px; }

  .somatic-intro { left: 468px; top: 163px; width: 294px; }
  .symptoms-title { position: absolute; left: 468px; top: 413px; font-weight: 400; font-size: 17px; line-height: 20px; }
  .symptoms-list { position: absolute; left: 523px; top: 473px; list-style: none; font-weight: 300; font-size: 16.5px; line-height: 19.2px; }
  .trauma-note { left: 468px; top: 741px; width: 294px; }

  .somatic-sessions { left: 853px; top: 124px; width: 282px; }
  .rest-text { left: 853px; top: 469px; width: 282px; }
</style>
</head>
<body>
<main class="brochure">
  <div class="backdrop-glow" role="img" aria-label="Faint lotus petals and sweeping golden arcs in the background"></div>
  <div class="brochure__frame"></div>

  <div class="photo-strip">
    <div class="photo-strip__portrait" role="img" aria-label="Portrait photo of the practitioner"></div>
    <div class="photo-strip__sunset" role="img" aria-label="Golden sunset over calm water"></div>
  </div>
  <span class="pointer" style="left:342px; top:228px;"></span>

  <div class="block credentials">
    <div class="credentials__name">Maren Rowe CMT</div>
    is a Somatic Renewal™ Practitioner, SRP<br>
    Certified Level III StillRest Teacher<br>
    Certified Sound Healing Practitioner -<br>
    Pacific Institute of Holistic Arts<br>
    Certified Transpersonal Breathwork Facilitator
  </div>

  <div class="block intro">
    <p>The services that I offer focus on supporting self-care, self-empowerment and self-regulation. Healing is returning home to our inherent sense of resiliency, vitality and well-being. I am honored to work with you and support you in your own unique journey home to yourself.</p>
  </div>

  <h2 class="services-title">3 unique separate services<br>that I offer:</h2>
  <ul class="services-list">
    <li>• Somatic Renewal</li>
    <li>• StillRest &amp; Yoga Nidra<br>&nbsp;&nbsp;&nbsp;Meditation</li>
    <li>• Sound Therapy</li>
  </ul>

  <h2 class="section-tab section-tab--somatic">Somatic Renewal™</h2>
  <span class="pointer" style="left:467px; top:133px;"></span>

  <div class="block somatic-intro">
    <p>Somatic Renewal is a body-oriented approach to resolving the symptoms of trauma and chronic stress. Sources of trauma are wide-ranging -- including accidents; falls; surgeries; injuries; physical assault; rape; emotional, physical or sexual abuse; loss of a loved one; childhood neglect or abuse; difficult births; high fever; serious illness; natural disasters, violence and war.</p>
  </div>

  <h3 class="symptoms-title">The Symptoms of Unresolved<br>Trauma can include:</h3>
  <ul class="symptoms-list">
    <li>•Panic or anxiety</li>
    <li>&nbsp;&nbsp;(including panic attacks)</li>
    <li>• Hyper-vigilance</li>
    <li>• Chronic pain of all kinds</li>
    <li>• Sleep disorders</li>
    <li>• Chronic tension</li>
    <li>• Addictions of all kinds</li>
    <li>• Migraines</li>
    <li>• Gastrointestinal disorders</li>
    <li>• Dissociation</li>
    <li>• And many others</li>
  </ul>

  <div class="block trauma-note">
    <p>Trauma occurs when the instinctual “high arousal” states of our survival responses (fight, flight and freeze) are unable to discharge, settle and regulate in response to threatening and overwhelming experiences. The result is that this highly charged energy remains stuck or “frozen” as an unresolved memory within the body.</p>
  </div>

  <div class="block somatic-sessions">
    <p>Somatic Renewal sessions assist clients to reconnect to their bodies and to gently discharge the stuck or “frozen” energies of trauma so that resiliency, stability and vitality are restored.</p>
    <p>I offer both Somatic Renewal™ bodywork and techniques in my private practice. I’m deeply inspired and grateful for the results that I’ve witnessed in my clients. Somatic Renewal is remarkable in its ability to bring healing and relief to the fear, hopelessness and pain of trauma.</p>
  </div>

  <h2 class="section-tab section-tab--rest">StillRest &amp; Yoga Nidra Meditation</h2>
  <span class="pointer" style="left:866px; top:458px;"></span>

  <div class="block rest-text">
    <p>StillRest (Guided Deep Rest) is a modern adaption of an ancient meditation practice called Yoga Nidra (yogic sleep). StillRest is a research based protocol that provides a systematic method for promoting healing, stress reduction and self-regulation. StillRest is used in the treatment of trauma, P.T.S.D., and many stress related illnesses; such as insomnia, chronic pain, anxiety and depression.</p>
    <p>I offer individual sessions of StillRest and personalized instruction in learning Yoga Nidra meditation. The deep relaxation of Yoga Nidra is very restorative as it allows for the release of physical, emotional and mental tension as your body rests in a reclined position. Yoga Nidra facilitates the ability to develop the “relaxation response” and is one of the most highly effective forms of stress reduction.</p>
  </div>
</main>
</body>
</html>
```